varnity.com car care product labeling with cut outs will be printed on holographic sheet.

Need to make label for eco-friendly car care products. no hazard signs.
clean and simple design minimalism
wheel cleaner
tire shiner
glass cleaner
all purpose cleaner
247x90mm
166x150mm

Target Market(s)

eco friendly car care products. europe , uae

Industry/Entity Type

car care products, eco-friendly product line

Requirements
Must have
• BW design print on holographic sheet/label .eco-friendly signs
Nice to have
• premium product look and simplicity will be at first place, can be with cut outs

```html
<!DOCTYPE html>
<html lang="en">
<head>
<meta charset="utf-8">
<title>varnity – car care labels</title>
<link rel="stylesheet" href="https://fonts.googleapis.com/css2?family=Montserrat:wght@700&family=Michroma&display=swap">
<style>
  :root {
    --page: #ffffff;
    --ink: #000000;
    --holo-violet: #7f8dc8;
    --holo-sky: #6ec9ee;
    --holo-cream: #fbf9ea;
    --holo-blush: #ecc3d2;
    --holo-magenta: #de80b3;
    --holo-rose: #f296a4;
    --holo-peach: #f7b9a0;
    --holo-butter: #f5e6b3;
    --holo-lime: #c7e0a8;
    --holo-teal: #93cbb4;
    --holo-blue: #4fa3dc;
    --holo-label: linear-gradient(61deg,
      var(--holo-violet) 0%,
      var(--holo-sky) 6%,
      var(--holo-cream) 16%,
      var(--holo-blush) 23%,
      var(--holo-magenta) 30%,
      var(--holo-rose) 38%,
      var(--holo-peach) 48%,
      var(--holo-butter) 57%,
      var(--holo-lime) 65%,
      var(--holo-teal) 72%,
      var(--holo-blue) 80%,
      var(--holo-violet) 88%,
      var(--holo-sky) 97%);
  }
  html, body {
    margin: 0;
    padding: 0;
    width: 1200px;
    height: 1200px;
    overflow: hidden;
    background: var(--page);
  }
  .sheet {
    position: relative;
    width: 1200px;
    height: 1200px;
  }
  .label {
    position: absolute;
    background: var(--holo-label);
  }
  .label--wheel { left: 33px; top: 33px; width: 722px; height: 653px; }
  .label--tire  { left: 29px; top: 742px; width: 1075px; height: 391px; }
  .brand {
    position: absolute;
    margin: 0;
    font-family: "Montserrat", sans-serif;
    font-weight: 700;
    font-size: 22px;
    line-height: 1;
    color: var(--ink);
    letter-spacing: 0.2px;
  }
  .label--wheel .brand { left: 223px; top: 36px; }
  .label--tire .brand  { left: 420px; top: 8px; }
  .label-art {
    position: absolute;
    inset: 0;
    width: 100%;
    height: 100%;
  }
  .product-name {
    font-family: "Michroma", sans-serif;
    fill: var(--ink);
  }
</style>
</head>
<body>
<main class="sheet">

  <section class="label label--wheel">
    <p class="brand">varnity</p>
    <svg class="label-art" viewBox="0 0 722 653" aria-hidden="false">
      <text class="product-name" transform="translate(374 417) rotate(-90)"
            font-size="37" textLength="344" lengthAdjust="spacingAndGlyphs">wheel  cleaner</text>
      <g class="wheel-icon" role="img" aria-label="Alloy wheel rim icon">
        <circle cx="361" cy="515" r="42" fill="var(--ink)"/>
        <circle cx="361" cy="515" r="36" fill="var(--holo-magenta)"/>
        <circle cx="361" cy="515" r="14" fill="var(--ink)"/>
      </g>
      <g class="eco-badge" role="img" aria-label="Eco-friendly certification badge">
        <circle cx="498" cy="597" r="22" fill="none" stroke="var(--ink)" stroke-width="1"/>
        <circle cx="498" cy="597" r="14" fill="var(--ink)"/>
      </g>
    </svg>
  </section>

  <section class="label label--tire">
    <p class="brand">varnity</p>
    <svg class="label-art" viewBox="0 0 1075 391">
      <text class="product-name" transform="translate(547 258) rotate(-90)"
            font-size="24" textLength="175" lengthAdjust="spacingAndGlyphs">tire  shiner</text>
      <g class="tire-icon">
        <circle cx="538" cy="299" r="23.5" fill="none" stroke="var(--ink)" stroke-width="6"/>
        <circle cx="538" cy="299" r="19" fill="none" stroke="var(--holo-peach)" stroke-width="0.8"/>
      </g>
      <g class="eco-badge" role="img" aria-label="Eco-friendly certification badge">
        <circle cx="635" cy="371" r="22" fill="none" stroke="var(--ink)" stroke-width="1"/>
        <circle cx="635" cy="371" r="14" fill="var(--ink)"/>
      </g>
    </svg>
  </section>

</main>
</body>
</html>
```